Personal Chef Business Card Design

My company, Simmerly, is a personal in-home chef service that caters to clients' needs, but I am not a caterer. The types of services that I provide range from : weekly menus for busy families, special menus for specific diets, custom menus, private parties, intimate dinners, and brunch parties. My cooking style is seasonal and simple with the option of a variety of cuisines. I like colorful and simple business cards. My business is just getting started as I will be the only employee for now. I would like to be able to use the design on the card for my logo also. I don't know if logo design is a different service altogether.

If you can convince me to go with double-sided, then so be it, but until then, I'll stick with singe-sided.

Target Market(s)

busy families, health conscious, private parties, brunch parties, dinner parties

Industry/Entity Type

Chef

Contact Information for Business Card

Owen Farley
owenfarley@mailbrook.net
571-806-3172
Simmerly Personal Chef Service
Serving the DC/VA/MD area

Font styles to use
Serif
Sans Serif
Decorative
Script
Other font styles liked:
• Anything

Requirements
Must have
• I will be using the illustration as my logo so that I can use it for promotional merchandise.

```html
<!DOCTYPE html>
<html lang="en">
<head>
<meta charset="utf-8">
<title>Simmerly Personal Chef Service – Business Card</title>
<link rel="stylesheet" href="https://fonts.googleapis.com/css2?family=Hind:wght@400;600;700&display=swap">
<style>
  :root {
    --backdrop: #e6e3df;
    --card: #fbfbfa;
    --brand-red: #c8282b;
    --rule-brown: #4a2a1c;
    --ink: #4a4440;
    --panel-cream: #f5efe4;
  }
  * { box-sizing: border-box; margin: 0; padding: 0; }
  html, body {
    width: 1200px;
    height: 1000px;
    overflow: hidden;
    background: var(--backdrop);
    font-family: "Hind", sans-serif;
  }
  .business-card {
    position: absolute;
    left: 165px;
    top: 250px;
    width: 870px;
    height: 500px;
    background: var(--card);
    box-shadow: 0 6px 18px rgba(0,0,0,0.12);
  }
  .brand-name {
    position: absolute;
    left: 95px;
    top: 62px;
    width: 690px;
    font-weight: 700;
    font-size: 148px;
    line-height: 1;
    letter-spacing: 2px;
    color: var(--brand-red);
    text-transform: uppercase;
    white-space: nowrap;
  }
  .rule {
    position: absolute;
    left: 95px;
    width: 680px;
    height: 2px;
    background: var(--rule-brown);
  }
  .rule::before, .rule::after {
    content: "";
    position: absolute;
    top: -2px;
    width: 12px;
    height: 6px;
    border-radius: 50%;
    background: var(--rule-brown);
  }
  .rule::before { left: -6px; }
  .rule::after { right: -6px; }
  .rule--top { top: 232px; }
  .rule--bottom { top: 300px; }
  .tagline {
    position: absolute;
    left: 95px;
    top: 244px;
    width: 680px;
    font-weight: 400;
    font-size: 29px;
    line-height: 1.5;
    color: var(--ink);
    white-space: nowrap;
  }
  .contact-panel {
    position: absolute;
    left: 95px;
    right: 100px;
    top: 302px;
    bottom: 0;
    background: var(--panel-cream);
    text-align: center;
    color: var(--ink);
    padding-top: 34px;
  }
  .contact-name {
    font-weight: 700;
    font-size: 34px;
    letter-spacing: 1px;
    text-transform: uppercase;
    line-height: 1.2;
  }
  .contact-email,
  .contact-phone {
    font-weight: 600;
    font-size: 27px;
    line-height: 1.35;
    letter-spacing: 0.5px;
  }
  .contact-phone { font-size: 29px; }
</style>
</head>
<body>
  <article class="business-card">
    <h1 class="brand-name">Simmerly</h1>
    <div class="rule rule--top"></div>
    <p class="tagline">Personal Chef Service Serving the DC/VA/MD Area</p>
    <div class="rule rule--bottom"></div>
    <section class="contact-panel">
      <p class="contact-name">Owen Farley</p>
      <p class="contact-email">owenfarley@mailbrook.net</p>
      <p class="contact-phone">571-806-3172</p>
    </section>
  </article>
</body>
</html>
```